Velmor Stationery Design

We need Business Card, Letterhead, #10 Envelope , 3" x 4" Mailing Label, and email signature block. Also need "Aircraft Services" added small under the logo on everything except the email signature block. "Aircraft Services" should be in a simple font to to conflict with or distract from the logo. Our address info is:
4817 Halvend Loop NW
Brantwick, GA 30592
P 555.208.3146
C 555.208.3146 (for biz cards only)
glen@velmorjet.example (for biz cards only)
Website velmorjet.example
Feel free to play around with colors but I expect that black or gray will work best for the address/phone info etc.

Target Market(s)

Aircraft owners

Industry/Entity Type

Aviation

Colors

Designer to choose only greyscale colors for use in the design.

Requirements
Must have
• Clean and sophisticated design -

```html
<!DOCTYPE html>
<html lang="en">
<head>
<meta charset="utf-8">
<title>Velmor Business Card</title>
<link href="https://fonts.googleapis.com/css2?family=Montserrat:wght@400;500;600&display=swap" rel="stylesheet">
<style>
  :root {
    --bg: #b9b8b3;
    --card-white: #ffffff;
    --card-black: #141414;
    --pattern-dark: #232323;
    --accent: #3a3a3a;
    --accent-light: #d6d6d6;
    --edge: #5c5c5c;
    --ink: #1c1c1c;
    --muted: #6a6a6a;
  }
  * { margin: 0; padding: 0; box-sizing: border-box; }
  html, body {
    width: 1200px; height: 857px; overflow: hidden;
    background: var(--bg);
    font-family: "Montserrat", sans-serif;
  }
  .stage {
    width: 1200px; height: 857px;
    display: flex; align-items: center; justify-content: center; gap: 44px;
  }
  .card {
    width: 520px; height: 297px;
    position: relative;
    border-bottom: 4px solid var(--edge);
    box-shadow: 0 10px 24px rgba(0,0,0,0.22);
  }
  .card-front { background: var(--card-white); }
  .card-back { background: var(--card-black); overflow: hidden; }

  .logo-lockup {
    display: flex; flex-direction: column; align-items: center; gap: 6px;
  }
  .wordmark {
    font-weight: 600;
    letter-spacing: 0.06em;
    text-transform: uppercase;
    line-height: 1;
  }
  .tagline {
    font-weight: 400;
    font-size: 10px;
    letter-spacing: 0.32em;
    text-transform: uppercase;
    line-height: 1;
  }
  .front-logo {
    position: absolute; left: 0; top: 0; width: 258px; height: 100%;
    display: flex; align-items: center; justify-content: center;
  }
  .front-logo .wordmark { font-size: 44px; color: var(--accent); }
  .front-logo .tagline { color: var(--muted); }

  .divider {
    position: absolute; left: 258px; top: 58px; width: 1.5px; height: 178px;
    background: var(--accent);
  }
  .contact {
    position: absolute; left: 284px; top: 50px;
    color: var(--ink); font-size: 12.5px; line-height: 1.45;
  }
  .contact .person-name {
    color: var(--accent); font-weight: 600; font-size: 16px;
    letter-spacing: 0.02em; line-height: 1.2;
  }
  .contact .person-title { font-size: 10.5px; color: var(--muted); margin-bottom: 14px; }
  .contact .address { margin-bottom: 12px; }
  .contact-row { display: flex; align-items: center; gap: 8px; }
  .contact-row svg { width: 11px; height: 11px; flex: none; }

  .back-pattern {
    position: absolute; inset: 0;
    background: linear-gradient(135deg, var(--card-black), var(--pattern-dark) 55%, var(--card-black));
  }
  .back-logo {
    position: absolute; left: 50%; top: 62%; transform: translate(-50%, -50%);
  }
  .back-logo .wordmark { font-size: 34px; color: var(--accent-light); }
  .back-logo .tagline { font-size: 8px; color: #9a9a9a; }
</style>
</head>
<body>
<main class="stage">
  <section class="card card-front">
    <div class="front-logo">
      <div class="logo-lockup">
        <span class="wordmark">Velmor</span>
        <span class="tagline">Aircraft Services</span>
      </div>
    </div>
    <div class="divider"></div>
    <div class="contact">
      <p class="person-name">MARCUS DELANE</p>
      <p class="person-title">Development Manager Officer</p>
      <p class="address">4817 Halvend Loop NW<br>Brantwick, GA 30592</p>
      <p class="contact-row">
        <svg viewBox="0 0 12 12" aria-hidden="true"><path d="M3 1l2 2.5-1.2 1.2a7 7 0 0 0 3.5 3.5L8.5 7 11 9l-1.2 1.8C6 11 1 6 1.2 2.2z" fill="var(--accent)"/></svg>
        555.208.3146
      </p>
      <p class="contact-row">
        <svg viewBox="0 0 12 12" aria-hidden="true"><rect x="3" y="0.8" width="6" height="10.4" rx="1" fill="none" stroke="var(--accent)" stroke-width="1.2"/></svg>
        555.208.3146
      </p>
      <p class="contact-row">
        <svg viewBox="0 0 12 12" aria-hidden="true"><rect x="0.5" y="2.5" width="11" height="7.5" fill="var(--accent)"/><path d="M0.5 2.5L6 7l5.5-4.5" fill="none" stroke="#fff" stroke-width="1"/></svg>
        glen@velmorjet.example
      </p>
      <p class="contact-row">
        <svg viewBox="0 0 12 12" aria-hidden="true"><circle cx="6" cy="6" r="5" fill="none" stroke="var(--accent)" stroke-width="1.2"/><path d="M1 6h10M6 1c-2.5 3-2.5 7 0 10M6 1c2.5 3 2.5 7 0 10" fill="none" stroke="var(--accent)" stroke-width="1"/></svg>
        velmorjet.example
      </p>
    </div>
  </section>

  <section class="card card-back">
    <div class="back-pattern" role="img" aria-label="Subtle tone-on-tone repeated brand pattern on black"></div>
    <div class="back-logo">
      <div class="logo-lockup">
        <span class="wordmark">Velmor</span>
        <span class="tagline">Aircraft Services</span>
      </div>
    </div>
  </section>
</main>
</body>
</html>
```